Newsletter Design Project

We need a template design for Mailchimp (html) newsletter (two types, one with only one property and one with several). One will be a b2b newsletter the other one a b2c.

It needs to work as a template in mailchimp and be branded like our website www.tide-vista-benalora.com

Reason: have not yet found the design that will be the one.

Target Market(s)

b2b: real estate agencies, b2c: real estate buyers in Spain in the middle and luxury segment: €350 k plus

Industry/Entity Type

Property

Requirements
Must have
• mailchimp compatible

```html
<!DOCTYPE html>
<html lang="en">
<head>
<meta charset="utf-8">
<title>Tide Vista Benalora – Special Offer</title>
<link rel="stylesheet" href="https://fonts.googleapis.com/css2?family=Arimo:wght@400;700&display=swap">
<style>
  :root {
    --page: #ffffff;
    --panel: #cfc17f;
    --ink: #1a1a1a;
    --black: #0d0d0d;
    --white: #ffffff;
    --rule: #3a3a2a;
    --muted: #555555;
    --social: #3b6fb0;
    --photo-pool: linear-gradient(160deg, #c98b4a 0%, #e0b36e 35%, #4fb7d4 60%, #2f8fb8 80%, #6a8a3c 100%);
    --photo-room: linear-gradient(150deg, #7a4a2a 0%, #b07a4c 50%, #e8d2b0 100%);
    --photo-bed: linear-gradient(150deg, #c7a47a 0%, #ead7b8 55%, #f5ece0 100%);
    --photo-garden: linear-gradient(170deg, #8fb4d8 0%, #d9c9a4 40%, #4f7a32 75%, #3a5e24 100%);
  }
  * { box-sizing: border-box; margin: 0; padding: 0; }
  html, body {
    width: 800px; height: 1200px; overflow: hidden;
    background: var(--page);
    font-family: "Arimo", Arial, sans-serif;
    color: var(--ink);
  }
  .newsletter { position: relative; width: 800px; height: 1200px; }

  .brand {
    position: absolute; top: 22px; left: 0; width: 800px;
    display: flex; justify-content: center; align-items: center; gap: 12px;
  }
  .brand-name {
    font-size: 30px; font-weight: 700; letter-spacing: 1px;
    text-transform: uppercase; color: var(--black);
  }
  .brand-mark { width: 26px; height: 26px; background: var(--black); }

  .offer-panel {
    position: absolute; left: 152px; top: 101px; width: 571px; height: 507px;
    background: var(--panel); border-radius: 6px;
  }
  .offer-title {
    position: absolute; left: 21px; top: 19px; width: 536px; height: 40px;
    background: var(--black); color: var(--white); border-radius: 4px;
    font-size: 17px; line-height: 40px; padding-left: 14px;
  }
  .offer-title strong { font-weight: 700; }

  .photo { position: absolute; }
  .photo-main { left: 21px; top: 67px; width: 536px; height: 171px; background: var(--photo-pool); }

  .facts { position: absolute; left: 21px; top: 256px; width: 200px; }
  .price {
    background: var(--black); color: var(--white);
    font-size: 13px; font-weight: 700; height: 30px; line-height: 30px; padding-left: 10px;
  }
  .fact-list { list-style: none; }
  .fact-list li {
    font-size: 10px; height: 16px; line-height: 15px; padding-left: 10px;
    border-bottom: 1px solid var(--rule);
  }

  .description {
    position: absolute; left: 248px; top: 252px; width: 300px;
    font-size: 11.5px; line-height: 15px;
  }
  .read-more {
    position: absolute; left: 248px; top: 350px; width: 107px; height: 22px;
    background: var(--black); color: var(--white); border-radius: 11px;
    font-size: 11px; line-height: 22px; text-align: center; text-decoration: none;
  }

  .gallery { position: absolute; left: 21px; top: 395px; width: 536px; display: flex; justify-content: space-between; }
  .gallery .photo { position: static; width: 112px; height: 80px; }
  .thumb-room { background: var(--photo-room); }
  .thumb-bed { background: var(--photo-bed); }
  .thumb-garden { background: var(--photo-garden); }

  .footer-note {
    position: absolute; left: 152px; top: 624px;
    font-size: 11px; line-height: 19px; color: var(--muted);
  }
  .social { position: absolute; left: 540px; top: 626px; display: flex; gap: 13px; }
  .social-link { display: block; width: 33px; height: 33px; border-radius: 5px; background: var(--social); }
</style>
</head>
<body>
<div class="newsletter">
  <header class="brand">
    <span class="brand-name">Tide Vista Benalora</span>
    <span class="brand-mark" aria-hidden="true"></span>
  </header>

  <main class="offer-panel">
    <h1 class="offer-title"><strong>Special Offer:</strong> Villa for Sale in Marbella</h1>
    <div class="photo photo-main" role="img" aria-label="Villa exterior with swimming pool, terrace and awning"></div>

    <div class="facts">
      <div class="price">PRICE: 650,000 €</div>
      <ul class="fact-list">
        <li>Beds: 5</li>
        <li>Baths: 5</li>
        <li>Built Size: 280</li>
        <li>Plot Size: 782</li>
      </ul>
    </div>

    <p class="description">A ready to move in to charming 5 bedroom villa in Marbella. The property has a private pool in a nicely kept garden. Inside one finds an ample living room and a large kitchen on the ground floor. Furthermore on the ground floor 4 bedrooms. The upper floor is dedicated to a large master bedroom with en suite bathroom.</p>
    <a class="read-more" href="#">Read More</a>

    <div class="gallery">
      <div class="photo thumb-room" role="img" aria-label="Living room interior"></div>
      <div class="photo thumb-bed" role="img" aria-label="Bedroom interior"></div>
      <div class="photo thumb-garden" role="img" aria-label="Garden and villa exterior"></div>
      <div class="photo thumb-bed" role="img" aria-label="Master bedroom interior"></div>
    </div>
  </main>

  <footer>
    <p class="footer-note">If you don't want to receive emails anymore - Unsubscribe<br>© TideVista All Right Reserved</p>
    <nav class="social" aria-label="Social media">
      <a class="social-link" href="#" aria-label="Social profile 1"></a>
      <a class="social-link" href="#" aria-label="Social profile 2"></a>
      <a class="social-link" href="#" aria-label="Social profile 3"></a>
      <a class="social-link" href="#" aria-label="Social profile 4"></a>
    </nav>
  </footer>
</div>
</body>
</html>
```